Business Card Design Project

Want a modern business card.
Concern is that our email address is long and thus poses a design challenge.
Items like the company name can be omitted from text as it will be available via the logo.

Example:
Desmond Farraway
President / CEO
Cell 555.304.2817
Office 555.619.0352
desmondf@qtvnetworkplatforms.example
www.qtvnetworkplatforms.example

Target Market(s)

Technical and executive level members of Information Technology companies in the Healthcare industry.

Industry/Entity Type

Business

Colors

Designer to choose colors to be used in the design.

Requirements
Nice to have
• Raised logo, but I am open.

```html
<!DOCTYPE html>
<html lang="en">
<head>
<meta charset="utf-8">
<title>QTV Network Platforms – Business Card</title>
<link rel="stylesheet" href="https://fonts.googleapis.com/css2?family=Arimo:wght@400;700&display=swap">
<style>
  :root {
    --backdrop: #2f2f2f;
    --card: #ffffff;
    --navy: #2b4a8f;
    --navy-deep: #1f3c80;
    --red: #d8272f;
    --card-w: 720px;
    --card-h: 411px;
  }
  * { box-sizing: border-box; margin: 0; padding: 0; }
  html, body {
    width: 1200px; height: 914px; overflow: hidden;
    background: var(--backdrop);
    font-family: "Arimo", Arial, sans-serif;
  }
  .sheet {
    position: relative; width: 1200px; height: 914px;
    display: flex; flex-direction: column; align-items: center;
    justify-content: center; gap: 32px;
  }
  .card {
    position: relative; width: var(--card-w); height: var(--card-h);
    background: var(--card); overflow: hidden;
    box-shadow: 0 10px 28px rgba(0,0,0,.45);
  }
  .card-shapes { position: absolute; inset: 0; width: 100%; height: 100%; }
  .wordmark {
    position: absolute; color: var(--navy); font-weight: 700;
    text-transform: uppercase; letter-spacing: .02em; line-height: 1.05;
  }
  .card-front .wordmark { left: 250px; top: 46px; font-size: 42px; text-align: right; }
  .card-back .wordmark { left: 52px; top: 214px; font-size: 38px; text-align: right; }
  .contact { position: absolute; left: 66px; top: 238px; color: var(--navy); }
  .contact-name { font-size: 21px; font-weight: 400; }
  .contact-title { font-size: 12px; color: var(--red); margin-top: 2px; margin-bottom: 12px; }
  .contact-list { list-style: none; }
  .contact-list li {
    display: flex; align-items: center; gap: 9px;
    font-size: 14.5px; line-height: 22px;
  }
  .contact-icon { width: 13px; height: 13px; flex: none; fill: var(--red); }
</style>
</head>
<body>
<main class="sheet">

  <section class="card card-front" aria-label="Business card front">
    <svg class="card-shapes" viewBox="0 0 720 411" preserveAspectRatio="none" aria-hidden="true">
      <defs>
        <linearGradient id="navyFade" x1="0" y1="0" x2="1" y2="1">
          <stop offset="0" stop-color="#3a5c9e"/>
          <stop offset="1" stop-color="#1f3c80"/>
        </linearGradient>
      </defs>
      <polygon points="24,0 720,0 720,32" fill="var(--navy)"/>
      <polygon points="272,218 720,218 720,411" fill="url(#navyFade)"/>
    </svg>
    <div class="wordmark">QTV Network<br>Platforms</div>
    <div class="contact">
      <p class="contact-name">Desmond Farraway</p>
      <p class="contact-title">President / CEO</p>
      <ul class="contact-list">
        <li><svg class="contact-icon" viewBox="0 0 16 16"><circle cx="8" cy="5" r="3.5"/><path d="M1 16c0-4 3-6.5 7-6.5s7 2.5 7 6.5z"/></svg>555.304.2817</li>
        <li><svg class="contact-icon" viewBox="0 0 16 16"><path d="M2 1h12v15H9.5v-3h-3v3H2z M4 3v2h2V3zm3 0v2h2V3zm3 0v2h2V3zM4 7v2h2V7zm3 0v2h2V7zm3 0v2h2V7z" fill-rule="evenodd"/></svg>555.619.0352</li>
        <li><svg class="contact-icon" viewBox="0 0 16 16"><circle cx="8" cy="8" r="7" fill="none" stroke="var(--red)" stroke-width="1.6"/><path d="M1 8h14M8 1c-3 3.5-3 10.5 0 14M8 1c3 3.5 3 10.5 0 14" fill="none" stroke="var(--red)" stroke-width="1.3"/></svg>www.qtvnetworkplatforms.example</li>
        <li><svg class="contact-icon" viewBox="0 0 16 16"><path d="M0 3h16v10H0z M1.5 4.5 8 9.5l6.5-5" fill="none" stroke="var(--red)" stroke-width="1.5"/></svg>desmondf@qtvnetworkplatforms.example</li>
      </ul>
    </div>
  </section>

  <section class="card card-back" aria-label="Business card back">
    <svg class="card-shapes" viewBox="0 0 720 411" preserveAspectRatio="none" aria-hidden="true">
      <defs>
        <linearGradient id="navyFadeBack" x1="0" y1="0" x2="1" y2="1">
          <stop offset="0" stop-color="#3a5c9e"/>
          <stop offset="1" stop-color="#1f3c80"/>
        </linearGradient>
      </defs>
      <polygon points="30,0 720,0 720,392" fill="url(#navyFadeBack)"/>
      <polygon points="12,0 30,0 720,392 720,411 708,411" fill="var(--red)"/>
    </svg>
    <div class="wordmark">QTV Network<br>Platforms</div>
  </section>

</main>
</body>
</html>
```